Business Card Design for Brisley Consulting

I need business cards for a new company I have started called Brisley Consulting. Brisley Consulting is a new business based out of Columbus Ohio. I will be operating in Ohio as well as nationwide. Brisley Consulting is a professional organization designed to fit your organization's specific needs. We are dedicated to the success of organizations. We handle human resource management, leadership coaching and development, executive training, team building, personality inventories and searches, performance evaluations, temp. services, custom solutions and more. Brisley consulting services a variety of industries such as government agencies, educational systems, board of directors, construction services and more, please visit our website for a full list of services (the website will be important).

I leave the design to you. I am a 45 year old male. I was in the education field for 21 years and 11 years as a superintendent. I like the colors red and black. Don't know what works, I will leave that to you as well. I would like to have it be catchy yet masculine. I have been associated with many organizations over the years both public and private, and will be reaching out to the public and private sector.

I do need a logo...so I leave that to you as well. Company name is Brisley Consulting.

Industry/Entity Type

Construction

Contact Information for Business Card

Gordon T. Brisley, President
Brisley Consulting
47 W.Ninth St. Suite 385
Arcade at Kelmont Court
Columbus, Ohio 43287

Phone : 330-418-2973
email : gbrisley@brisleyadvise.com
web : www.brisleyadvise.com
twitter : @brisleyadvise
facebook : Brisley Consulting

```html
<!DOCTYPE html>
<html lang="en">
<head>
<meta charset="utf-8">
<title>Brisley Consulting – Business Card</title>
<link rel="stylesheet" href="https://fonts.googleapis.com/css2?family=Cinzel:wght@400;700&display=swap">
<style>
  :root {
    --band-blue: #3d8ff0;
    --accent-red: #fe0016;
    --ink: #111111;
    --paper: #ffffff;
  }
  html, body {
    margin: 0;
    padding: 0;
    overflow: hidden;
    background: var(--paper);
  }
  .card {
    position: relative;
    width: 1200px;
    height: 686px;
    overflow: hidden;
    background: var(--paper);
    font-family: "Cinzel", serif;
    color: var(--ink);
  }
  .top-band {
    position: absolute;
    left: 0; top: 0;
    width: 1200px; height: 16px;
    background: var(--band-blue);
  }
  .bottom-band {
    position: absolute;
    left: 0; top: 666px;
    width: 640px; height: 20px;
    background: var(--band-blue);
  }
  .name-tab {
    position: absolute;
    left: 0; top: 53px;
    width: 43px; height: 139px;
    background: var(--band-blue);
  }
  .red-field {
    position: absolute;
    left: 0; top: 0;
  }
  .holder {
    position: absolute;
    left: 55px; top: 66px;
    white-space: nowrap;
  }
  .holder-name {
    margin: 0;
    font-size: 31px;
    font-weight: 700;
    line-height: 1.2;
  }
  .holder-title {
    margin: 4px 0 0;
    font-size: 31px;
    font-weight: 400;
    line-height: 1.2;
  }
  .contact {
    position: absolute;
    left: 660px; top: 208px;
    list-style: none;
    margin: 0; padding: 0;
    white-space: nowrap;
  }
  .contact li {
    display: flex;
    align-items: center;
  }
  .contact-icon {
    width: 48px;
    flex: none;
  }
  .contact-phone { font-size: 36px; height: 50px; }
  .contact-email { font-size: 20px; height: 46px; margin-top: 2px; }
  .contact-web   { font-size: 20px; height: 46px; }
  .address {
    position: absolute;
    left: 565px; top: 420px;
    margin: 0;
    font-style: normal;
    font-size: 30px;
    line-height: 51px;
    white-space: nowrap;
  }
  .brand-mark {
    position: absolute;
    left: 140px; top: 360px;
    width: 150px; height: 150px;
    background: var(--accent-red);
  }
  .brand-name {
    position: absolute;
    left: 43px; top: 558px;
    margin: 0;
    font-size: 32px;
    font-weight: 700;
    white-space: nowrap;
  }
</style>
</head>
<body>
<div class="card">
  <div class="top-band"></div>
  <div class="bottom-band"></div>

  <svg class="red-field" width="1200" height="686" viewBox="0 0 1200 686" aria-hidden="true">
    <ellipse cx="990" cy="470" rx="475" ry="350" fill="var(--accent-red)"/>
  </svg>

  <div class="name-tab"></div>
  <div class="holder">
    <p class="holder-name">Gordon T. Brisley</p>
    <p class="holder-title">President</p>
  </div>

  <ul class="contact">
    <li class="contact-phone">
      <svg class="contact-icon" width="46" height="30" viewBox="0 0 46 30" aria-hidden="true">
        <path d="M2 10 Q23 -2 44 10 L44 14 L34 14 L33 9 Q23 6 13 9 L12 14 L2 14 Z" fill="var(--ink)"/>
        <path d="M10 16 L36 16 L42 29 L4 29 Z" fill="var(--ink)"/>
        <circle cx="23" cy="22" r="4" fill="var(--accent-red)"/>
      </svg>
      <span>330-418-2973</span>
    </li>
    <li class="contact-email">
      <svg class="contact-icon" width="40" height="22" viewBox="0 0 40 22" aria-hidden="true">
        <rect x="4" y="3" width="32" height="17" fill="var(--ink)"/>
        <path d="M4 3 L20 14 L36 3" fill="none" stroke="var(--accent-red)" stroke-width="2"/>
      </svg>
      <span>gbrisley@brisleyadvise.com</span>
    </li>
    <li class="contact-web">
      <svg class="contact-icon" width="46" height="40" viewBox="0 0 46 40" aria-hidden="true">
        <g fill="none" stroke="var(--ink)" stroke-width="2.5">
          <circle cx="21" cy="20" r="17"/>
          <ellipse cx="21" cy="20" rx="8" ry="17"/>
          <line x1="4" y1="20" x2="38" y2="20"/>
          <path d="M7 11 H35 M7 29 H35"/>
        </g>
      </svg>
      <span>www.brisleyadvise.com</span>
    </li>
  </ul>

  <address class="address">
    47 W.Ninth St. Suite 385<br>
    Arcade at Kelmont Court Columbus<br>
    Ohio 43287
  </address>

  <div class="brand-mark"></div>
  <p class="brand-name">Brisley Consulting</p>
</div>
</body>
</html>
```